Business cards for Home & Garden Design business
Oakvale Grove Design
Business cards for Home & Garden Design business - Home and Garden
Creative Brief
Bright & Fun-filled
Marla Pendby
Designer
PO Box 732 Winkler, MB R6W 2K9
marlapendby@oakvalegrovedesign.example
oakvalegrovedesign.example
Would love to have my logo on a background of a rustic, white fence/door, or white birch trees. Question - do you already have access to my logo, or how do I upload it?

```html
<!DOCTYPE html>
<html lang="en">
<head>
<meta charset="utf-8">
<title>Oakvale Grove Design – Business Cards</title>
<link href="https://fonts.googleapis.com/css2?family=Montserrat:wght@400;600&display=swap" rel="stylesheet">
<style>
  :root {
    --backdrop: #e4e5e6;
    --card-dark: #26262c;
    --card-light: #ffffff;
    --teal: #3f9ca2;
    --ink: #2b2b30;
    --ink-soft: #6d6d74;
    --rule: #9a9aa0;
  }
  html, body {
    margin: 0;
    padding: 0;
    width: 1200px;
    height: 946px;
    overflow: hidden;
    background: var(--backdrop);
    font-family: "Montserrat", Arial, sans-serif;
  }
  .canvas {
    position: relative;
    width: 1200px;
    height: 946px;
  }
  .card {
    position: absolute;
    border-radius: 22px;
    overflow: hidden;
    box-shadow: 0 14px 30px rgba(0,0,0,0.18);
  }
  .card--back {
    left: 300px;
    top: 50px;
    width: 600px;
    height: 340px;
    background: var(--card-dark);
    display: flex;
    align-items: center;
    justify-content: center;
  }
  .card--front {
    left: 220px;
    top: 440px;
    width: 760px;
    height: 440px;
    background: var(--card-light);
  }
  .brand {
    display: flex;
    align-items: center;
    gap: 12px;
    color: var(--teal);
    font-weight: 600;
    letter-spacing: 0.5px;
  }
  .brand__dot {
    width: 16px;
    height: 16px;
    border-radius: 50%;
    background: var(--teal);
    flex: none;
  }
  .card--back .brand { font-size: 34px; }
  .card--front .brand {
    position: absolute;
    left: 48px;
    top: 128px;
    font-size: 27px;
  }
  .divider {
    position: absolute;
    left: 408px;
    top: 70px;
    width: 1px;
    height: 215px;
    background: var(--rule);
  }
  .contact {
    position: absolute;
    left: 432px;
    top: 70px;
    color: var(--ink);
  }
  .contact__name {
    font-size: 15px;
    font-weight: 600;
    letter-spacing: 1px;
    text-transform: uppercase;
    margin: 0;
  }
  .contact__title {
    font-size: 11px;
    color: var(--ink-soft);
    margin: 3px 0 16px;
  }
  .contact__address {
    font-size: 11px;
    line-height: 1.5;
    color: var(--ink-soft);
    margin: 0 0 16px;
  }
  .contact__list {
    list-style: none;
    margin: 0;
    padding: 0;
    font-size: 11px;
    color: var(--ink-soft);
  }
  .contact__list li {
    display: flex;
    align-items: center;
    gap: 9px;
    height: 19px;
  }
  .icon {
    width: 12px;
    height: 12px;
    fill: var(--ink);
    flex: none;
  }
  .swoosh {
    position: absolute;
    left: 0;
    bottom: 0;
    width: 760px;
    height: 440px;
  }
</style>
</head>
<body>
<main class="canvas">

  <section class="card card--back" aria-label="Business card back">
    <div class="brand"><span class="brand__dot"></span>Oakvale Grove Design</div>
  </section>

  <section class="card card--front" aria-label="Business card front">
    <svg class="swoosh" viewBox="0 0 760 440" aria-hidden="true">
      <path d="M0 318 C 180 330, 420 410, 760 392 L760 440 L0 440 Z" fill="var(--card-dark)"/>
      <path d="M0 306 C 180 318, 420 396, 760 380" fill="none" stroke="var(--teal)" stroke-width="7"/>
    </svg>

    <div class="brand"><span class="brand__dot"></span>Oakvale Grove Design</div>

    <div class="divider"></div>

    <div class="contact">
      <p class="contact__name">Marla Pendby</p>
      <p class="contact__title">Managing Director</p>
      <p class="contact__address">PO Box 732<br>Winkler, MB R6W 2K9</p>
      <ul class="contact__list">
        <li>
          <svg class="icon" viewBox="0 0 12 12"><path d="M3 1 L5 3.5 L4 5 C4.6 6.4 5.6 7.4 7 8 L8.5 7 L11 9 L10 11 C5 11 1 7 1 2 Z"/></svg>
          204 555 0132
        </li>
        <li>
          <svg class="icon" viewBox="0 0 12 12"><rect x="3" y="1" width="6" height="10" rx="1.2"/></svg>
          204 555 0147
        </li>
        <li>
          <svg class="icon" viewBox="0 0 12 12"><rect x="1" y="4" width="10" height="6" rx="1"/><rect x="3" y="1" width="6" height="3"/></svg>
          204 555 0158
        </li>
        <li>
          <svg class="icon" viewBox="0 0 12 12"><circle cx="6" cy="6" r="5.5"/></svg>
          marlapendby@oakvalegrovedesign.example
        </li>
        <li>
          <svg class="icon" viewBox="0 0 12 12"><circle cx="6" cy="6" r="5" fill="none" stroke="var(--ink)" stroke-width="1.3"/><path d="M1 6 H11 M6 1 C3.5 4 3.5 8 6 11 M6 1 C8.5 4 8.5 8 6 11" fill="none" stroke="var(--ink)" stroke-width="1"/></svg>
          oakvalegrovedesign.example
        </li>
      </ul>
    </div>
  </section>

</main>
</body>
</html>
```